Construction Company Stationary Design

We have previously utilised MakerHive to develop a new logo, we wanted to implement it for a while to ensure we liked it before rolling out new stationary. The time has come and we require:
Business Cards
"With Compliments" Cards
Asset Stickers
Vehicle Stickers
Letterhead
Document Header
Invoice Header
Cover Page
We are an established Construction Company working in Northern Australia (outback) that is venturing into a more corporate environment. We DO NOT do residential construction, we focus on commercial & government (Defence, schools, health etc) and work in both urban and remote environments.
Business Card Requirements:
• Logo
• Company Name
• Staff Name
• Staff Position
• Company Physical & Postal Address
• ABN
• Staff Mobile
• Staff Direct Phone (if applicable)
• Staff Email
• Office Phone
• Office Fax
"With Compliments" cards to be much the same as the business cards but with company details only (no staff details)
Asset stickers again to be much the same but with a space to write in asset number.
Document header requires 4 spaces to enter details much like our previous one attached.
We appreciate that designers time is valuable and would request that samples only be produced for one or two of the required items (say Business Card & Letterhead) and await a feedback score of 4 or more prior to producing the full suite of stationary.
If you require any further information please do not hesitate to contact me. lionel@brevmark.com.au

```html
<!DOCTYPE html>
<html lang="en">
<head>
<meta charset="utf-8">
<title>Ridgeline Constructions – Business Card</title>
<link href="https://fonts.googleapis.com/css2?family=Jost:wght@300;400&family=Montserrat:wght@700&family=Open+Sans:wght@400&display=swap" rel="stylesheet">
<style>
  :root {
    --paper: #ffffff;
    --charcoal: #15191b;
    --ink: #111111;
    --accent: #f04a12;
    --stripe: #5b5f61;
    --text-light: #f4f4f4;
  }
  html, body {
    margin: 0;
    padding: 0;
    width: 1200px;
    height: 720px;
    overflow: hidden;
    background: var(--paper);
  }
  .card {
    position: relative;
    width: 1200px;
    height: 720px;
    background: var(--paper);
    overflow: hidden;
  }
  .brand {
    position: absolute;
    left: 108px;
    top: 86px;
    width: 380px;
    color: var(--ink);
    font-family: "Montserrat", sans-serif;
    font-weight: 700;
    text-transform: uppercase;
    letter-spacing: 2px;
  }
  .brand-mark {
    width: 64px;
    height: 64px;
    background: var(--accent);
    margin-bottom: 18px;
  }
  .brand-name {
    display: block;
    font-size: 52px;
    line-height: 1.05;
  }
  .brand-sub {
    display: block;
    font-size: 29px;
    line-height: 1.3;
    letter-spacing: 1px;
  }
  .accent-rule {
    position: absolute;
    left: 0;
    top: 350px;
    width: 100%;
    height: 5px;
    background: var(--accent);
  }
  .base {
    position: absolute;
    left: 0;
    top: 359px;
    width: 100%;
    height: 361px;
    background: var(--charcoal);
  }
  .hazard-strip {
    position: absolute;
    left: 0;
    top: 4px;
    width: 100%;
    height: 6px;
    background: repeating-linear-gradient(135deg, var(--stripe) 0 8px, transparent 8px 16px);
  }
  .staff {
    position: absolute;
    left: 89px;
    top: 112px;
  }
  .staff-name {
    margin: 0;
    font-family: "Jost", sans-serif;
    font-weight: 300;
    font-size: 57px;
    line-height: 1;
    color: var(--accent);
  }
  .staff-role {
    margin: 10px 0 0 -5px;
    font-family: "Jost", sans-serif;
    font-weight: 400;
    font-size: 25px;
    color: var(--text-light);
  }
  .contact {
    position: absolute;
    left: 662px;
    top: 68px;
    margin: 0;
    padding: 0;
    list-style: none;
    font-family: "Open Sans", sans-serif;
    font-size: 25px;
    color: var(--text-light);
  }
  .contact-item {
    display: flex;
    align-items: center;
    height: 61px;
  }
  .contact-icon {
    width: 40px;
    height: 34px;
    margin-right: 24px;
    fill: var(--accent);
  }
  .contact-address {
    margin-top: 2px;
    padding-left: 7px;
  }
</style>
</head>
<body>
<main class="card">
  <header class="brand">
    <div class="brand-mark"></div>
    <span class="brand-name">Ridgeline</span>
    <span class="brand-sub">Constructions</span>
  </header>

  <div class="accent-rule"></div>

  <section class="base">
    <div class="hazard-strip"></div>

    <div class="staff">
      <h1 class="staff-name">Martin Kessler</h1>
      <p class="staff-role">General Manager</p>
    </div>

    <ul class="contact">
      <li class="contact-item">
        <svg class="contact-icon" viewBox="0 0 40 34" aria-hidden="true">
          <path d="M9 2 l6 -1 l3 9 l-4 3 c2 5 5 8 9 10 l3 -4 l9 3 l-1 7 c-1 2 -3 3 -6 3 C16 30 7 21 6 7 c0 -3 1 -4 3 -5z"/>
          <path d="M24 4 a10 10 0 0 1 9 9 l-2 0 a8 8 0 0 0 -7 -7z"/>
        </svg>
        <span>+61 8 8945 2210 , FAX#</span>
      </li>
      <li class="contact-item">
        <svg class="contact-icon" viewBox="0 0 40 34" aria-hidden="true">
          <path d="M2 4 h36 v3 l-18 12 l-18 -12z"/>
          <path d="M2 11 l18 12 l18 -12 v19 h-36z"/>
        </svg>
        <span>info@ridgelinebuild.com</span>
      </li>
      <li class="contact-item">
        <svg class="contact-icon" viewBox="0 0 40 34" aria-hidden="true">
          <path d="M4 9 l6 -6 a5 5 0 0 1 7 0 l5 5 a5 5 0 0 1 0 7 l-2 2 l-3 -3 l2 -2 a1.5 1.5 0 0 0 0 -2 l-4 -4 a1.5 1.5 0 0 0 -2 0 l-5 5 a1.5 1.5 0 0 0 0 2 l4 4 l-3 3 l-5 -4 a5 5 0 0 1 0 -7z"/>
          <path d="M36 25 l-6 6 a5 5 0 0 1 -7 0 l-5 -5 a5 5 0 0 1 0 -7 l2 -2 l3 3 l-2 2 a1.5 1.5 0 0 0 0 2 l4 4 a1.5 1.5 0 0 0 2 0 l5 -5 a1.5 1.5 0 0 0 0 -2 l-4 -4 l3 -3 l5 4 a5 5 0 0 1 0 7z"/>
        </svg>
        <span>www.ridgelinebuild.com</span>
      </li>
      <li class="contact-address">2041 Copper Rd Darwin, NT 0800</li>
    </ul>
  </section>
</main>
</body>
</html>
```